Innovative global company needs a design for an attractive customer business quote

We need a design for a business quote which is a written offer from a seller to a prospective buyer. Business quotes are often a key step in the complex sales process.

Our company brings human insight to business by studying how people work, wherever they work. Those insights can help organizations achieve a higher level of performance, by creating places that unlock the promise of their people. We are a global, publicly traded company.

Guidelines:
Version 1: Use all the data from the example to product an attractive looking quote using every bit of detail. It should clearly explain to a customer what there order will look like.
Version 2: Use a subset of the data (highlighted on second document) to product a leaner/cleaner looking quote.

• All versions need to use the product illustrations for a quick visual reference to the reader (in zip file, image files named by catalog number).
• The output should be scalable to US Letter and European A4
• The quote should look professional but not stuffy.
• Color is OK to use (no red)
• Make sure you leave space for a logo, along with company information.
• Should be light and airy with white space
Updates

The design needs to be creative and unique. We are ok with it being drastically different as long as it has the content.

I want 2 versions, one with all the data and the other with just the text highlighted in yellow.
I want this quote to be readable and easy for customers to understand.
the vertical lines are not required, in fact it would be nice to see a design without those vertical lines

Industry/Entity Type

Business

Font styles to use
Sans Serif

Requirements
Must have
• 2 versions submitted:
One is with all the data
Second is the subset of the data (note the highlighted text).

Both version must have Art.

```html
<!DOCTYPE html>
<html lang="en">
<head>
<meta charset="utf-8">
<title>Quotation 2327</title>
<link href="https://fonts.googleapis.com/css2?family=Arimo:wght@400;700&family=Lexend:wght@400;500&display=swap" rel="stylesheet">
<style>
  :root {
    --ink-blue: #2c2f94;
    --band-blue: #2b2e96;
    --text: #3a3a3a;
    --muted: #555;
    --rule: #c9c9c9;
    --page: #ffffff;
    --backdrop: #ffffff;
    --header-top: #ffffff;
    --header-bottom: #e4e6ea;
    --art-grey: #cfd1d4;
    --art-dark: #5a5d62;
  }
  * { box-sizing: border-box; margin: 0; padding: 0; }
  html, body { width: 952px; height: 1200px; overflow: hidden; background: var(--backdrop); }
  body { font-family: "Arimo", Arial, sans-serif; color: var(--text); }

  .stage { position: absolute; left: 0; top: 0; width: 900px; height: 1130px;
           transform: scale(1.0578, 1.0619); transform-origin: 0 0; }

  .sheet { position: absolute; left: 51px; top: 51px; width: 798px; height: 1034px;
           background: var(--page); border: 1px solid #444;
           box-shadow: 2px 3px 8px rgba(0,0,0,.35); overflow: hidden; }

  .masthead { position: absolute; left: 0; top: 0; width: 100%; height: 162px;
              background: radial-gradient(ellipse at 50% 0%, var(--header-top) 30%, var(--header-bottom) 100%); }
  .masthead h1 { position: absolute; right: 47px; top: 40px; font-family: "Lexend", sans-serif;
                 font-weight: 400; font-size: 36px; color: var(--ink-blue); letter-spacing: -0.5px; }

  .meta { position: absolute; left: 0; top: 162px; width: 100%; }
  .meta-head { height: 35px; background: var(--band-blue); position: relative; }
  .meta-values { height: 36px; border-bottom: 1px solid var(--rule); position: relative; }
  .cell { position: absolute; transform: translateX(-50%); text-align: center; white-space: nowrap; }
  .meta-head .cell { top: 7px; font-family: "Lexend", sans-serif; font-size: 9.5px; line-height: 10.5px;
                     color: #fff; text-transform: uppercase; }
  .meta-values .cell { top: 12px; font-size: 12px; color: var(--text); }

  .party { position: absolute; top: 268px; }
  .party-label { position: absolute; top: 0; font-family: "Lexend", sans-serif; font-weight: 500;
                 font-size: 15px; color: var(--ink-blue); white-space: nowrap; letter-spacing: -0.3px; }
  .party-address { position: absolute; top: 0; font-size: 14px; line-height: 17.5px; color: var(--muted); white-space: nowrap; }
  .party-address strong { color: #444; }

  .items-head { position: absolute; left: 0; top: 369px; width: 100%; height: 35px; background: var(--band-blue); }
  .items-head .cell { font-family: "Lexend", sans-serif; font-size: 9.5px; line-height: 10.5px; color: #fff;
                      text-transform: uppercase; top: 12px; }
  .items-head .cell.two-line { top: 6px; }

  .line-item { position: absolute; left: 0; width: 100%; border-bottom: 1px solid var(--rule); }
  .line-item .num { position: absolute; top: 10px; font-size: 12px; color: var(--muted); transform: translateX(-50%); }
  .line-item .money { position: absolute; top: 10px; font-size: 12px; color: var(--muted); text-align: right; }
  .desc { position: absolute; left: 198px; top: 10px; font-size: 11px; line-height: 14.3px; color: #444; }
  .desc .title { font-weight: 700; }
  .desc .options-label { font-weight: 700; margin-top: 10px; }
  .desc ul { list-style: none; padding-left: 10px; }
  .desc li::before { content: "\2022\00a0"; }
  .product-art { position: absolute; }

  .terms { position: absolute; left: 35px; top: 937px; }
  .terms .party-label { position: static; display: inline-block; margin-right: 26px; }
  .terms span.value { font-size: 14px; color: var(--muted); }

  .totals { position: absolute; left: 534px; top: 908px; width: 263px; }
  .total-row { display: flex; height: 34px; margin-bottom: 1px; }
  .total-row .label { width: 159px; background: var(--band-blue); color: #fff; font-family: "Lexend", sans-serif;
                      font-size: 10px; text-transform: uppercase; text-align: right; padding: 11px 15px 0 0; }
  .total-row .amount { flex: 1; border-bottom: 1px solid var(--rule); font-size: 11px; font-weight: 700;
                       color: #444; text-align: right; padding: 11px 10px 0 0; }
  .total-row .label.centered { text-align: center; padding-right: 0; }
</style>
</head>
<body>
<div class="stage">
  <div class="sheet">
    <header class="masthead"><h1>Quotation</h1></header>

    <section class="meta">
      <div class="meta-head">
        <div class="cell" style="left:72px">Quote<br>Number</div>
        <div class="cell" style="left:187px">Quote<br>Date</div>
        <div class="cell" style="left:320px">Customer<br>Order Number</div>
        <div class="cell" style="left:450px">Customer<br>Number</div>
        <div class="cell" style="left:595px">Account<br>Representative</div>
        <div class="cell" style="left:746px">Project<br>ID</div>
      </div>
      <div class="meta-values">
        <div class="cell" style="left:72px">2327</div>
        <div class="cell" style="left:187px">4/10/2014</div>
        <div class="cell" style="left:320px">1467942</div>
        <div class="cell" style="left:450px">35</div>
        <div class="cell" style="left:595px">Dana Whitfield</div>
        <div class="cell" style="left:746px">abc1</div>
      </div>
    </section>

    <section class="party">
      <div class="party-label" style="left:35px">QUOTE TO:</div>
      <div class="party-address" style="left:149px"><strong>Northfield Works</strong><br>420 Lakeshore Avenue<br>Harbor Bend, MI 49999</div>
      <div class="party-label" style="left:469px">SHIP TO:</div>
      <div class="party-address" style="left:571px"><strong>Northfield Works</strong><br>420 Lakeshore Avenue<br>Harbor Bend, MI 49999</div>
    </section>

    <div class="items-head">
      <div class="cell" style="left:53px">Line</div>
      <div class="cell" style="left:146px">Quantity</div>
      <div class="cell" style="left:392px">Model Number / Description</div>
      <div class="cell two-line" style="left:646px">Unit<br>Price</div>
      <div class="cell two-line" style="left:746px">Extended<br>Amount</div>
    </div>

    <article class="line-item" style="top:404px;height:158px">
      <div class="num" style="left:53px">1</div>
      <div class="num" style="left:146px">5</div>
      <div class="desc">
        <div class="title">Meridian Freestanding; Desk-Corner<br>24D x 36W</div>
        Basic: Mist<br>Edge: Black<br>Top-Surf: Black
        <div class="options-label">Options:</div>
        <ul><li>Scallops</li><li>3 Corner Supports</li><li>Half Height Modesty Panel</li></ul>
      </div>
      <svg class="product-art" style="left:526px;top:14px" width="58" height="44" role="img" aria-label="Product illustration: corner desk">
        <rect width="58" height="44" fill="var(--art-dark)" opacity=".55" rx="3"/>
      </svg>
      <div class="money" style="right:116px">$850.00</div>
      <div class="money" style="right:15px">$850.00</div>
    </article>

    <article class="line-item" style="top:562px;height:158px">
      <div class="num" style="left:53px">2</div>
      <div class="num" style="left:146px">2</div>
      <div class="desc">
        <div class="title">Tower, Door hinged left hand with drawers<br>24D x 15 1/2W x 72 5/8H</div>
        Basic: Black<br>Front: Black<br>Lock: Ember Chrome
        <div class="options-label">Options:</div>
        <ul><li>Glass Door (Ice White)</li><li>Bar Pull (Polished Chrome)</li><li>Dovetail Construction</li></ul>
      </div>
      <svg class="product-art" style="left:533px;top:14px" width="52" height="136" role="img" aria-label="Product illustration: storage tower">
        <rect width="52" height="136" fill="var(--art-grey)" opacity=".7"/>
      </svg>
      <div class="money" style="right:116px">$850.00</div>
      <div class="money" style="right:15px">$850.00</div>
    </article>

    <article class="line-item" style="top:720px;height:188px">
      <div class="num" style="left:53px">3</div>
      <div class="num" style="left:146px">2</div>
      <div class="desc">
        <div class="title">Bench, Package quantity 6, media: vista<br>24D x 180W</div>
        Basic: Fieldstone<br>Front: Fieldstone
        <div class="options-label">Options:</div>
        <ul><li>Oakridge Maintenance Service: 1 Year</li><li>Top-Surf: Laminate (Black)</li><li>Edge: Plastic (Black)</li><li>2 Shrouds for 40in Monitors: Textured Paint (Black)</li><li>Loop Leg</li><li>HDMI Digital</li></ul>
      </div>
      <svg class="product-art" style="left:529px;top:26px" width="54" height="36" role="img" aria-label="Product illustration: bench workstation">
        <rect width="54" height="36" fill="var(--art-grey)" opacity=".7" rx="3"/>
      </svg>
      <div class="money" style="right:116px">$850.00</div>
      <div class="money" style="right:15px">$850.00</div>
    </article>

    <section class="terms">
      <div class="party-label">TERMS:</div><span class="value">Due Upon Receipt</span>
    </section>

    <section class="totals">
      <div class="total-row"><div class="label">Subtotal</div><div class="amount">$5,300.00</div></div>
      <div class="total-row"><div class="label centered">Michigan Non-Taxable</div><div class="amount">$318.00</div></div>
      <div class="total-row"><div class="label">Grand Total</div><div class="amount">$5,618.00</div></div>
    </section>
  </div>
</div>
</body>
</html>
```